Redesign my wordpress blog

I would like a brand new look to my popular www.brightmorninglist.com website.
Would like you to install it for me and make it work.

My slogan is
If you always do what you always did then you always get what you always got.

I would like a simple design, very visual to show photos however it may be that not all posts have photo's.

Colors
edf7fa
cee9f5
86cfc7
fbf289
85acd3
ffffff
86cfc6

Requirements
Must have
• Instagram
Featured posts
social share
mailchimp - I all ready have this.

```html
<!DOCTYPE html>
<html lang="en">
<head>
<meta charset="utf-8">
<title>Bright Morning List</title>
<link href="https://fonts.googleapis.com/css2?family=Source+Sans+3:wght@400;600;700&display=swap" rel="stylesheet">
<style>
:root{
  --page:#edf7fa;
  --card:#dcf0f6;
  --tag:#cee9f5;
  --teal:#86cfc7;
  --teal-dark:#45a99d;
  --yellow:#e2d23c;
  --blue:#85acd3;
  --ink:#2f3a3d;
  --muted:#6f8a90;
  --line:#d3e6ec;
  --white:#ffffff;
  --brand:#3f4a4d;
}
*{box-sizing:border-box;margin:0;padding:0}
html,body{width:1200px;height:2571px;overflow:hidden}
body{background:var(--page);font-family:"Source Sans 3",sans-serif;color:var(--ink);position:relative}
a{color:inherit;text-decoration:none}
.abs{position:absolute}

.brand{left:197px;top:38px}
.brand-name{font-weight:700;font-size:22px;color:var(--brand);line-height:1}
.nav{left:441px;top:42px;display:flex;gap:36px;font-weight:700;font-size:18px;color:#4a5558;width:573px;justify-content:space-between}
.search{left:789px;top:90px;width:222px;height:32px;border:1px solid #c9e3ea;border-radius:4px;background:#e4f3f7;font-size:12px;font-style:italic;color:var(--teal-dark);padding:8px 12px}
.search svg{position:absolute;right:10px;top:7px}
.rule{left:191px;width:823px;height:1px;background:var(--line)}

.section-title{left:191px;top:196px;font-size:29px;font-weight:600;color:var(--teal)}
.carousel{left:189px;top:257px;display:flex;gap:20px}
.slide{width:190px}
.slide .ph{height:124px;border:1px solid #c8dde3}
.slide p{margin-top:9px;font-size:11px;line-height:16px;color:var(--teal-dark)}
.arrow{top:300px}

.tabs{left:191px;top:468px;display:flex;font-size:12.5px;color:var(--teal-dark)}
.tabs span{width:139px}
.tabs .active{color:var(--yellow)}

.sidebar{left:191px;top:530px;width:274px}
.side-h{font-size:13px;font-weight:700;letter-spacing:.3px;color:#3f4a4d;padding:8px 0 10px;border-bottom:1px solid var(--line);border-top:1px solid var(--line);margin-bottom:16px}
.signup{display:flex;gap:8px;margin-bottom:40px}
.signup .field{width:193px;height:30px;background:var(--white);border:1px solid #c9dde3;border-radius:3px;font-size:11px;color:#7a8a8e;padding:7px 10px}
.signup .btn{width:73px;height:30px;background:var(--teal-dark);color:var(--white);border-radius:3px;font-size:11px;text-align:center;line-height:30px}
.mini{display:flex;gap:8px;height:88px}
.mini .ph{width:66px;height:60px;border:3px solid var(--white);box-shadow:1px 2px 4px rgba(0,0,0,.25);flex:none}
.mini h4{font-size:12px;line-height:16px;font-weight:600;color:var(--teal-dark)}
.meta{display:flex;gap:18px;align-items:center;font-size:11px;color:var(--teal-dark);margin-top:5px;white-space:nowrap}
.meta i{display:inline-block;width:12px;height:11px;border:1.5px solid var(--teal-dark);border-radius:2px;vertical-align:-1px;margin-right:6px}
.meta i.bubble{border-radius:50%;background:var(--teal-dark)}
.list{margin-bottom:30px}
.insta{margin-bottom:13px}
.insta .ph{width:169px;height:167px;border:4px solid var(--white);box-shadow:1px 2px 5px rgba(0,0,0,.25);margin-left:4px}
.insta p{font-size:11px;line-height:16px;color:var(--teal-dark);margin-top:6px;width:180px}

.posts{left:497px;top:531px;width:517px}
.post{position:relative;background:var(--card);padding:36px 30px 0 30px;margin-bottom:53px}
.post::after{content:"";position:absolute;left:0;right:0;bottom:-14px;height:14px;background:radial-gradient(ellipse at top,rgba(0,0,0,.35),rgba(0,0,0,0) 70%)}
.post h2{font-size:16px;line-height:20px;font-weight:700;color:var(--teal-dark);width:300px}
.post .excerpt{font-size:11px;line-height:16.5px;width:300px;margin-top:14px;color:var(--ink)}
.post .ph{position:absolute;right:3px;top:37px;width:175px;height:139px;border:4px solid var(--white);box-shadow:1px 2px 4px rgba(0,0,0,.25)}
.tags{display:flex;gap:16px;margin-top:20px;font-size:14px;line-height:20px;color:var(--teal-dark)}
.tags .pill{background:#c3e5ef;color:#7fb9c9;font-size:11px;padding:1px 13px;border-radius:10px;height:20px}

.ph-window{background:linear-gradient(135deg,#4a5a3a,#b9a77a 45%,#2d2a26)}
.ph-bakery{background:linear-gradient(160deg,#2b2a26,#57503f 50%,#1d1c1a)}
.ph-tools{background:linear-gradient(135deg,#eee9e6,#cfc5c0 50%,#e7e2de)}
.ph-coast{background:linear-gradient(180deg,#3f7fd2,#5f9ad6 45%,#4e8a5a)}

.footer{left:0;width:1200px;top:2504px;text-align:center;font-size:11.5px;color:var(--teal-dark)}
</style>
</head>
<body>

<div class="abs brand"><span class="brand-name">Bright Morning List</span></div>
<nav class="abs nav"><a>HOME</a><a>ABOUT</a><a>BUY THE BOOK</a><a>WORKING WITH</a><a>CONTACT</a></nav>
<div class="abs search">Type your keyword
  <svg width="16" height="16" viewBox="0 0 16 16"><circle cx="7" cy="7" r="5" fill="none" stroke="#b7d6de" stroke-width="1.5"/><line x1="10.5" y1="10.5" x2="14" y2="14" stroke="#b7d6de" stroke-width="1.5"/></svg>
</div>
<div class="abs rule" style="top:176px"></div>

<h1 class="abs section-title">Featured Photos</h1>
<svg class="abs arrow" style="left:156px" width="16" height="26" viewBox="0 0 16 26"><polyline points="13,2 3,13 13,24" fill="none" stroke="var(--teal)" stroke-width="3"/></svg>
<svg class="abs arrow" style="left:1031px" width="16" height="26" viewBox="0 0 16 26"><polyline points="3,2 13,13 3,24" fill="none" stroke="var(--teal)" stroke-width="3"/></svg>
<div class="abs carousel">
  <div class="slide"><div class="ph ph-tools" role="img" aria-label="Brushes, tweezers and a compact laid out on a white surface"></div><p>5 Things to do for well-groomed Eyebrows from lashlane.com</p></div>
  <div class="slide"><div class="ph ph-window" role="img" aria-label="Shop window of a design studio with an oval mirror"></div><p>5 things to do in Geneva by Mara Lindqvist</p></div>
  <div class="slide"><div class="ph ph-bakery" role="img" aria-label="Bakery shop front with a lettered awning"></div><p>Have a sticky bun at Marlowe Bakehouse in Covent Garden London.</p></div>
  <div class="slide"><div class="ph ph-coast" role="img" aria-label="Seafront promenade with blue sky and palm trees"></div><p>5 Things to do at the 2014 Riviera Film Week.</p></div>
</div>

<div class="abs rule" style="top:456px"></div>
<div class="abs tabs"><span class="active">Recent activity</span><span>▾ Recent posts</span><span>Recent images</span><span>☇ RSS for recent posts</span></div>
<div class="abs rule" style="top:497px"></div>

<aside class="abs sidebar">
  <h3 class="side-h">SUBSCRIBE TO EMAIL UPDATES</h3>
  <div class="signup"><div class="field">Your email address</div><div class="btn">Subscribe</div></div>

  <h3 class="side-h">FEATURED POSTS</h3>
  <div class="list">
    <div class="mini"><div class="ph ph-window" role="img" aria-label="Design studio shop window"></div><div><h4>5 things to do in Geneva by Mara Lindqvist</h4><div class="meta"><span><i></i>19 Jan 2013</span><span><i class="bubble"></i>3 Comments</span></div></div></div>
    <div class="mini"><div class="ph ph-window" role="img" aria-label="Design studio shop window"></div><div><h4>5 things to do in Geneva by Mara Lindqvist</h4><div class="meta"><span><i></i>19 Jan 2013</span><span><i class="bubble"></i>3 Comments</span></div></div></div>
    <div class="mini"><div class="ph ph-window" role="img" aria-label="Design studio shop window"></div><div><h4>5 things to do in Geneva by Mara Lindqvist</h4><div class="meta"><span><i></i>19 Jan 2013</span><span><i class="bubble"></i>3 Comments</span></div></div></div>
    <div class="mini"><div class="ph ph-window" role="img" aria-label="Design studio shop window"></div><div><h4>5 things to do in Geneva by Mara Lindqvist</h4><div class="meta"><span><i></i>19 Jan 2013</span><span><i class="bubble"></i>3 Comments</span></div></div></div>
  </div>

  <h3 class="side-h">POPULAR POSTS</h3>
  <div class="list">
    <div class="mini"><div class="ph ph-window" role="img" aria-label="Design studio shop window"></div><div><h4>5 things to do in Geneva by Mara Lindqvist</h4><div class="meta"><span><i></i>19 Jan 2013</span><span><i class="bubble"></i>3 Comments</span></div></div></div>
    <div class="mini"><div class="ph ph-window" role="img" aria-label="Design studio shop window"></div><div><h4>5 things to do in Geneva by Mara Lindqvist</h4><div class="meta"><span><i></i>19 Jan 2013</span><span><i class="bubble"></i>3 Comments</span></div></div></div>
    <div class="mini"><div class="ph ph-window" role="img" aria-label="Design studio shop window"></div><div><h4>5 things to do in Geneva by Mara Lindqvist</h4><div class="meta"><span><i></i>19 Jan 2013</span><span><i class="bubble"></i>3 Comments</span></div></div></div>
    <div class="mini"><div class="ph ph-window" role="img" aria-label="Design studio shop window"></div><div><h4>5 things to do in Geneva by Mara Lindqvist</h4><div class="meta"><span><i></i>19 Jan 2013</span><span><i class="bubble"></i>3 Comments</span></div></div></div>
  </div>

  <h3 class="side-h">PHOTOS FROM INSTAGRAM</h3>
  <div class="insta"><div class="ph ph-window" role="img" aria-label="Design studio shop window with oval mirror"></div><p>5 things to do in Geneva by Mara Lindqvist</p></div>
  <div class="insta"><div class="ph ph-bakery" role="img" aria-label="Bakery shop front"></div><p>Have a sticky bun at Marlowe Bakehouse in Covent Garden London</p></div>
  <div class="insta"><div class="ph ph-window" role="img" aria-label="Design studio shop window"></div><p>5 things to do at Harbour Fish Bar at The Grand Quay Hotel, London</p></div>
  <div class="insta"><div class="ph ph-bakery" role="img" aria-label="Bakery shop front"></div><p>Run With The Stride Running Club</p></div>
</aside>

<main class="abs posts">
  <article class="post" style="height:322px">
    <h2>5 things to do in Geneva by Mara Lindqvist</h2>
    <div class="ph ph-window" role="img" aria-label="Design studio shop window with oval mirror"></div>
    <p class="excerpt">This post is a guest post from Mara Lindqvist. She is the owner of Fernleaf Design Studio in Geneva, Switzerland. 1. To start the day, I check out my boutique Fernleaf Design in Geneva and browse through its selection of contemporary home accessories. Strongly influenced by the swinging sixties, the shop offers trendy, fun yet elegant objects and small furniture. I make...</p>
    <div class="meta" style="margin-top:12px"><span><i></i>19 Jan 2013</span><span><i class="bubble"></i>3 Comments</span></div>
    <div class="tags"><span class="pill">Tags</span><span>Bright Morning List, Away from the UK,<br>Cities, Design</span></div>
  </article>
  <article class="post" style="height:333px">
    <h2>Have a sticky bun at Marlowe Bakehouse in Covent Garden London</h2>
    <div class="ph ph-bakery" role="img" aria-label="Bakery shop front with lettered awning"></div>
    <p class="excerpt">Covent Garden in Central London seems to be getting busier and busier. If you want a break from the crowds then you could do a lot worse than visiting Marlowe Bakehouse on Russell street (not far from the opera house) for a high quality bread based snack. Both sweet things and savory things are on offer. One Enjoy the finest Sticky Bun you will have ever...</p>
    <div class="meta" style="margin-top:12px"><span><i></i>19 Jan 2013</span><span><i class="bubble"></i>3 Comments</span></div>
    <div class="tags"><span class="pill">Tags</span><span>Bright Morning List, Away from the UK,<br>Cities, Design</span></div>
  </article>
  <article class="post" style="height:323px">
    <h2>Have a sticky bun at Marlowe Bakehouse in Covent Garden London</h2>
    <div class="ph ph-bakery" role="img" aria-label="Bakery shop front with lettered awning"></div>
    <p class="excerpt">Covent Garden in Central London seems to be getting busier and busier. If you want a break from the crowds then you could do a lot worse than visiting Marlowe Bakehouse on Russell street (not far from the opera house) for a high quality bread based snack. Both sweet things and savory things are on offer. One Enjoy the finest Sticky Bun you will have ever...</p>
    <div class="meta" style="margin-top:12px"><span><i></i>19 Jan 2013</span><span><i class="bubble"></i>3 Comments</span></div>
    <div class="tags"><span class="pill">Tags</span><span>Bright Morning List, Away from the UK,<br>Cities, Design</span></div>
  </article>
  <article class="post" style="height:323px">
    <h2>5 things to do in Geneva by Mara Lindqvist</h2>
    <div class="ph ph-window" role="img" aria-label="Design studio shop window with oval mirror"></div>
    <p class="excerpt">This post is a guest post from Mara Lindqvist. She is the owner of Fernleaf Design Studio in Geneva, Switzerland. 1. To start the day, I check out my boutique Fernleaf Design in Geneva and browse through its selection of contemporary home accessories. Strongly influenced by the swinging sixties, the shop offers trendy, fun yet elegant objects and small furniture. I make...</p>
    <div class="meta" style="margin-top:12px"><span><i></i>19 Jan 2013</span><span><i class="bubble"></i>3 Comments</span></div>
    <div class="tags"><span class="pill">Tags</span><span>Bright Morning List, Away from the UK,<br>Cities, Design</span></div>
  </article>
  <article class="post" style="height:332px">
    <h2>Have a sticky bun at Marlowe Bakehouse in Covent Garden London</h2>
    <div class="ph ph-bakery" role="img" aria-label="Bakery shop front with lettered awning"></div>
    <p class="excerpt">Covent Garden in Central London seems to be getting busier and busier. If you want a break from the crowds then you could do a lot worse than visiting Marlowe Bakehouse on Russell street (not far from the opera house) for a high quality bread based snack. Both sweet things and savory things are on offer. One Enjoy the finest Sticky Bun you will have ever...</p>
    <div class="meta" style="margin-top:12px"><span><i></i>19 Jan 2013</span><span><i class="bubble"></i>3 Comments</span></div>
    <div class="tags"><span class="pill">Tags</span><span>Bright Morning List, Away from the UK,<br>Cities, Design</span></div>
  </article>
</main>

<footer class="abs footer">Copyright © 2014 brightmorninglist &nbsp;•&nbsp; Contact me &nbsp;•&nbsp; RSS Feed</footer>

</body>
</html>
```